Signage for Brightwell Academy - Exterior

Size 32 ft x 5 ft 11 inches. It will be installed at a height of 25 feet. Should contain the Logo, Address, some courses to give an idea about what we do. The signage is installed on the 2nd floor, so the minimum size of letters would be as in the old signage design attached. The font size of the bottom line of our existing signage is as small as we should go. Basically it should be such that the first glance gives us an idea that it is a Brightwell Academy. You are allowed to change the logo colors, but the font and design will remain the same.
Updates

Reason: some extra time might be needed to improve the designs and get new inputs. need some out of the box designing.

Target Market(s)

High School and College going teens who wish to learn software skills for graphics and animation

Industry/Entity Type

Education

Font styles to use
Other font styles liked:
• Utopia

Colors

Designer to choose colors to be used in the design.

Requirements
Must have
• Logo, Address, Phone Number, website address, what we do.
• 1. Please refer to the image of our old signage uploaded. The font size of the courses mentioned at the bottom of the signage "ANIMATION, GAMING.." is the smallest size which is legible from the ground level.
• 2. We would like at least the web address in legible font size and if possible the phone number too. The physical address could be a little smaller as in the old signage, as that is not a calling factor and in case someone is interested, they can walk closer and read the address.
• 3. The calling factors would be a few courses and some graphics depicting what we do in the first look.
• 4.You are allowed to change the logo colors, but the font and design will remain the same. Prefer usage of Ubuntu font for text.
• 5. Prefer minimalist look and not cluttered. I feel mentioning more courses is making the signage cluttered. we can limit it to 3 courses.
Nice to have
• Graphics to suggest what we do. It should be eye catching. The graphic should be such that speaks of what we do. It should be suggestive.
Should not have
• It should not be too busy

```html
<!DOCTYPE html>
<html lang="en">
<head>
<meta charset="utf-8">
<title>Brightwell Academy – Exterior Signage</title>
<link rel="stylesheet" href="https://fonts.googleapis.com/css2?family=Ubuntu:wght@400;500;700&display=swap">
<style>
  :root {
    --backdrop: #2a2a2a;
    --band-start: #4527cc;
    --band-mid: #5b34a9;
    --band-end: #8e5173;
    --text-light: #ffffff;
    --accent-yellow: #f4e81c;
  }
  * { margin: 0; padding: 0; box-sizing: border-box; }
  html, body {
    width: 1200px;
    height: 435px;
    overflow: hidden;
    background: var(--backdrop);
    font-family: "Ubuntu", sans-serif;
  }
  .canvas {
    position: relative;
    width: 1200px;
    height: 435px;
  }
  .sign {
    position: absolute;
    left: 40px;
    top: 128px;
    width: 1120px;
    height: 178px;
    overflow: hidden;
    background: linear-gradient(90deg, var(--band-start) 0%, var(--band-mid) 45%, var(--band-end) 100%);
    color: var(--text-light);
  }
  .brand-name {
    position: absolute;
    left: 30px;
    top: 9px;
    font-weight: 400;
    font-size: 88px;
    line-height: 72px;
    letter-spacing: 10px;
    text-transform: uppercase;
    color: var(--text-light);
    white-space: nowrap;
  }
  .brand-name span { display: block; }
  .info {
    position: absolute;
    left: 480px;
    top: 29px;
  }
  .headline {
    font-weight: 700;
    font-size: 40px;
    letter-spacing: 1.5px;
    line-height: 40px;
    text-transform: uppercase;
    white-space: nowrap;
  }
  .courses {
    display: flex;
    gap: 50px;
    margin-top: 11px;
    list-style: none;
  }
  .course {
    display: flex;
    align-items: center;
    gap: 8px;
    font-size: 27px;
    line-height: 27px;
    letter-spacing: 0.5px;
    white-space: nowrap;
  }
  .course svg { width: 22px; height: 22px; flex: none; }
  .web {
    display: flex;
    align-items: center;
    gap: 18px;
    margin-top: 10px;
    font-size: 50px;
    line-height: 50px;
    white-space: nowrap;
  }
  .web svg { width: 34px; height: 34px; flex: none; }
  .web-name { color: var(--accent-yellow); }
  .web-tld { color: var(--text-light); }
</style>
</head>
<body>
<main class="canvas">
  <section class="sign" aria-label="Brightwell Academy exterior sign">
    <h1 class="brand-name"><span>Bright</span><span>well</span></h1>

    <div class="info">
      <h2 class="headline">Digital Academy</h2>
      <ul class="courses">
        <li class="course">
          <svg viewBox="0 0 20 20" aria-hidden="true"><circle cx="10" cy="10" r="8.2" fill="none" stroke="var(--accent-yellow)" stroke-width="2"/><path d="M6 10.3l2.8 2.8L14.3 7" fill="none" stroke="var(--accent-yellow)" stroke-width="2" stroke-linecap="round" stroke-linejoin="round"/></svg>
          VFX
        </li>
        <li class="course">
          <svg viewBox="0 0 20 20" aria-hidden="true"><circle cx="10" cy="10" r="8.2" fill="none" stroke="var(--accent-yellow)" stroke-width="2"/><path d="M6 10.3l2.8 2.8L14.3 7" fill="none" stroke="var(--accent-yellow)" stroke-width="2" stroke-linecap="round" stroke-linejoin="round"/></svg>
          GAMING
        </li>
        <li class="course">
          <svg viewBox="0 0 20 20" aria-hidden="true"><circle cx="10" cy="10" r="8.2" fill="none" stroke="var(--accent-yellow)" stroke-width="2"/><path d="M6 10.3l2.8 2.8L14.3 7" fill="none" stroke="var(--accent-yellow)" stroke-width="2" stroke-linecap="round" stroke-linejoin="round"/></svg>
          ANIMATION
        </li>
      </ul>
      <p class="web">
        <svg viewBox="0 0 32 32" aria-hidden="true">
          <circle cx="16" cy="16" r="15" fill="var(--text-light)"/>
          <g fill="none" stroke="var(--band-mid)" stroke-width="1.5">
            <circle cx="16" cy="16" r="9"/>
            <ellipse cx="16" cy="16" rx="4" ry="9"/>
            <line x1="7" y1="16" x2="25" y2="16"/>
            <line x1="16" y1="7" x2="16" y2="25"/>
            <path d="M8.5 11.5h15M8.5 20.5h15"/>
          </g>
        </svg>
        <span><span class="web-name">brightwell</span><span class="web-tld">.in</span></span>
      </p>
    </div>
  </section>
</main>
</body>
</html>
```